Business Card design for law firm = Juriskite Australia

We are seeking a new design for our business cards.
We are keeping our logo, which is attached.
We need space for
Name
Title
Address is , which is
Level 14
82 Penhallow Street
Sydney NSW 2000
Phone :
Mobile :
Fax :
Email :
DX :
website www.juriskite.com.au

Industry/Entity Type

Law Firm / Banking and Finance

Contact Information for Business Card

We are seeking a new design for our business cards. We are keeping our logo. We need space for Name Title Address is Level 14 82 Penhallow Street Sydney NSW 2000 Phone Mobile Fax Email DX website www.juriskite.com.au

Colors
0054AA
0677BA
7BADD7
CADEEF
E8F1F8

Requirements
Must have
• see our website for general feel www.juriskite.com.au

```html
<!DOCTYPE html>
<html lang="en">
<head>
<meta charset="utf-8">
<title>Juriskite Australia — Business Card</title>
<link rel="stylesheet" href="https://fonts.googleapis.com/css2?family=EB+Garamond:wght@500&family=Montserrat:wght@400;700&display=swap">
<style>
  :root {
    --stage: #0079b8;
    --paper: #ffffff;
    --brand-deep: #0d4db5;
    --brand-mid: #0677ba;
    --ink-grey: #555a60;
  }
  * { box-sizing: border-box; margin: 0; padding: 0; }
  html, body { width: 1200px; height: 1056px; overflow: hidden; }
  body {
    background: var(--stage);
    position: relative;
    font-family: "Montserrat", sans-serif;
  }
  .card {
    position: absolute;
    width: 600px;
    height: 343px;
    background: var(--paper);
    box-shadow: 0 14px 30px rgba(0, 0, 0, 0.18);
  }
  .card--front { left: 110px; top: 150px; }
  .card--back { left: 490px; top: 560px; }

  .wordmark {
    font-family: "EB Garamond", serif;
    font-weight: 500;
    color: var(--brand-deep);
    line-height: 1;
  }
  .card--front .wordmark {
    position: absolute;
    left: 42px;
    top: 34px;
    font-size: 44px;
  }

  .address {
    position: absolute;
    left: 42px;
    top: 150px;
    font-size: 13px;
    line-height: 1.35;
    color: var(--ink-grey);
  }
  .contact-list {
    position: absolute;
    left: 42px;
    top: 202px;
    list-style: none;
    font-size: 13px;
    line-height: 1.45;
    color: var(--ink-grey);
  }
  .contact-list li { display: flex; align-items: center; gap: 7px; }
  .contact-list svg { width: 11px; height: 11px; fill: var(--brand-mid); flex: none; }

  .person {
    position: absolute;
    right: 42px;
    top: 150px;
    text-align: right;
  }
  .person__name {
    font-weight: 700;
    font-size: 22px;
    letter-spacing: 0.5px;
    color: var(--brand-deep);
  }
  .person__title {
    margin-top: 4px;
    font-size: 14px;
    color: var(--ink-grey);
  }
  .person__rule {
    margin: 8px 0 0 auto;
    width: 88px;
    height: 2px;
    background: var(--brand-mid);
  }

  .lockup {
    position: absolute;
    left: 0; right: 0; top: 0; bottom: 0;
    display: flex;
    align-items: center;
    justify-content: center;
    gap: 16px;
  }
  .lockup__square {
    width: 46px;
    height: 46px;
    background: var(--brand-mid);
  }
  .card--back .wordmark { font-size: 54px; }
</style>
</head>
<body>
  <section class="card card--front" aria-label="Business card front">
    <div class="wordmark">Juriskite</div>

    <p class="address">Level 14 82 Penhallow Street<br>Sydney NSW 2000</p>

    <ul class="contact-list">
      <li><svg viewBox="0 0 12 12" aria-hidden="true"><path d="M1 4c0-2 2-3 5-3s5 1 5 3l-2 1-1-1H4L3 5zM3 6h6l1 5H2z"/></svg>+61-555-0142</li>
      <li><svg viewBox="0 0 12 12" aria-hidden="true"><path d="M3 1l2 2-1 2c1 1 2 2 3 3l2-1 2 2-2 2C5 11 1 7 1 3z"/></svg>+61-555-0198</li>
      <li><svg viewBox="0 0 12 12" aria-hidden="true"><path d="M3 1h6v3H3zM1 5h10v5H9V8H3v2H1zM3 9h6v2H3z"/></svg>+61-0555-01736</li>
      <li><svg viewBox="0 0 12 12" aria-hidden="true"><path d="M1 2h10v8H1zM2 3l4 3 4-3v1L6 7 2 4z" fill-rule="evenodd"/></svg>info@juriskite.com.au</li>
      <li><svg viewBox="0 0 12 12" aria-hidden="true"><circle cx="6" cy="6" r="5"/></svg>www.juriskite.com.au</li>
    </ul>

    <div class="person">
      <div class="person__name">MARA ELLISON</div>
      <div class="person__title">Director / CEO</div>
      <div class="person__rule"></div>
    </div>
  </section>

  <section class="card card--back" aria-label="Business card back">
    <div class="lockup">
      <span class="lockup__square"></span>
      <span class="wordmark">Juriskite</span>
    </div>
  </section>
</body>
</html>
```